hi all

Im after a new age looking business card with my company logo on it

must include these details, I would like the PH and Email to be symbols

If the colours used for card could be kept within the colours used in logo that I have supplied that would be great, if another colour is to be used dark grey would be ok. no light bulbs etc thanks

Details below to be incorporated on card

Damian Holloway

Lic E871302

PH 0219647381

E info@brightvaleelectrical.example.nz

Domestic Commercial Industrial Electricians

```html
<!DOCTYPE html>
<html lang="en">
<head>
<meta charset="utf-8">
<title>Brightvale Electrical – Business Card</title>
<link rel="stylesheet" href="https://fonts.googleapis.com/css2?family=Roboto:wght@400;500;700&display=swap">
<style>
  :root {
    --backdrop: #2b2b2b;
    --brand-blue: #1273bf;
    --brand-blue-deep: #0f64a8;
    --paper: #ffffff;
  }
  * { margin: 0; padding: 0; box-sizing: border-box; }
  html, body {
    width: 1125px;
    height: 1200px;
    overflow: hidden;
    background: var(--backdrop);
    font-family: "Roboto", Arial, sans-serif;
  }
  .canvas { position: relative; width: 1125px; height: 1200px; }

  .card { position: absolute; overflow: hidden; }

  /* Front */
  .card-front {
    left: 176px; top: 106px; width: 826px; height: 471px;
    background: var(--paper);
  }
  .front-band {
    position: absolute; inset: 0; width: 100%; height: 100%;
  }

  .brand {
    position: absolute; left: 58px; top: 78px;
    display: flex; align-items: center; gap: 16px;
    color: var(--brand-blue); font-weight: 700;
  }
  .brand-dot {
    width: 62px; height: 62px; border-radius: 50%;
    background: var(--brand-blue);
  }
  .brand-name { line-height: 1; letter-spacing: 1px; }
  .brand-name .line-main { display: block; font-size: 42px; }
  .brand-name .line-sub { display: block; font-size: 17px; letter-spacing: 4px; margin-top: 6px; text-align: right; }

  .contact {
    position: absolute; right: 37px; top: 290px;
    text-align: right; color: var(--paper);
  }
  .contact-name { font-size: 27px; font-weight: 700; line-height: 1; }
  .contact-role { font-size: 19px; font-weight: 500; margin-top: 6px; }
  .contact-line {
    font-size: 18px; font-weight: 400; line-height: 1;
    display: flex; justify-content: flex-end; align-items: center; gap: 8px;
  }
  .contact-licence { margin-top: 18px; }
  .contact-phone { margin-top: 10px; }
  .contact-email { margin-top: 8px; }
  .contact-line svg { width: 15px; height: 15px; fill: var(--paper); }

  /* Back */
  .card-back {
    left: 167px; top: 634px; width: 844px; height: 481px;
    background: var(--brand-blue); color: var(--paper);
  }
  .back-brand {
    position: absolute; left: 0; right: 0; top: 170px;
    display: flex; align-items: center; justify-content: center; gap: 22px;
    font-weight: 700;
  }
  .back-brand .brand-dot { width: 84px; height: 84px; background: var(--paper); }
  .back-brand .brand-name .line-main { font-size: 56px; }
  .back-brand .brand-name .line-sub { font-size: 22px; letter-spacing: 6px; margin-top: 8px; }

  .services {
    position: absolute; left: 0; right: 0; top: 394px;
    display: flex; justify-content: center; align-items: center; gap: 14px;
    font-size: 19px; font-weight: 400;
  }
  .services .sep { width: 6px; height: 6px; border-radius: 50%; background: var(--paper); }
</style>
</head>
<body>
<main class="canvas">

  <section class="card card-front" aria-label="Business card front">
    <svg class="front-band" viewBox="0 0 826 471" preserveAspectRatio="none" role="img" aria-label="Blue curved band sweeping across the lower right of the card">
      <defs>
        <linearGradient id="bandFill" x1="0" y1="0" x2="1" y2="1">
          <stop offset="0" stop-color="#1273bf"/>
          <stop offset="1" stop-color="#0f64a8"/>
        </linearGradient>
      </defs>
      <path d="M0 360 C 110 420, 200 450, 280 440 C 440 420, 580 230, 720 150 C 760 130, 795 132, 826 140 L 826 471 L 0 471 Z" fill="url(#bandFill)"/>
    </svg>

    <div class="brand">
      <span class="brand-dot"></span>
      <span class="brand-name">
        <span class="line-main">BRIGHTVALE</span>
        <span class="line-sub">ELECTRICAL</span>
      </span>
    </div>

    <div class="contact">
      <p class="contact-name">DAMIAN HOLLOWAY</p>
      <p class="contact-role">President</p>
      <p class="contact-line contact-licence">LIC : E871302</p>
      <p class="contact-line contact-phone">0219647381
        <svg viewBox="0 0 24 24" aria-label="Phone"><path d="M6.6 10.8a15.1 15.1 0 0 0 6.6 6.6l2.2-2.2c.3-.3.7-.4 1-.2 1.1.4 2.3.6 3.6.6.6 0 1 .4 1 1V20c0 .6-.4 1-1 1A17 17 0 0 1 3 4c0-.6.4-1 1-1h3.5c.6 0 1 .4 1 1 0 1.3.2 2.5.6 3.6.1.3 0 .7-.2 1z"/></svg>
      </p>
      <p class="contact-line contact-email">info@brightvaleelectrical.example.nz
        <svg viewBox="0 0 24 24" aria-label="Email"><path d="M2 5h20v14H2z M3 6l9 7 9-7" fill="#ffffff" stroke="#1273bf" stroke-width="1.5"/></svg>
      </p>
    </div>
  </section>

  <section class="card card-back" aria-label="Business card back">
    <div class="back-brand">
      <span class="brand-dot"></span>
      <span class="brand-name">
        <span class="line-main">BRIGHTVALE</span>
        <span class="line-sub">ELECTRICAL</span>
      </span>
    </div>
    <p class="services">
      <span>Domestic</span><span class="sep"></span>
      <span>Commercial</span><span class="sep"></span>
      <span>Industrial</span><span class="sep"></span>
      <span>Electricians</span>
    </p>
  </section>

</main>
</body>
</html>
```